60th Anniversary banner ad for e-mail signature

We need to have a banner designed for our email signature block which incorporates our logo as well as a 60th Anniversary statement. Size is 2" wide x 3/4" height. Design needs to be simple, incorporate the two colors of our logo (PMS 541C and 377M), with no borders.

We are a small company manufacturing screen printing inks, located in the Los Angeles area.

```html
<!DOCTYPE html>
<html lang="en">
<head>
<meta charset="UTF-8">
<title>60th Anniversary Banner</title>
<link rel="stylesheet" href="https://fonts.googleapis.com/css2?family=Kaushan+Script&display=swap">
<style>
  :root {
    --brand-green: #6b8e00;
    --brand-blue: #13467a;
    --paper: #ffffff;
  }
  html, body {
    margin: 0;
    padding: 0;
    width: 1200px;
    height: 450px;
    overflow: hidden;
    background: var(--paper);
  }
  .banner {
    display: block;
    width: 1200px;
    height: 450px;
  }
  .band { fill: var(--brand-green); }
  .headline,
  .brand-name {
    font-family: "Kaushan Script", cursive;
    font-weight: 400;
    fill: var(--brand-blue);
  }
  .headline__number { font-size: 150px; }
  .headline__ordinal { font-size: 82px; }
  .headline__word { font-size: 150px; }
  .brand-name { font-size: 40px; }
  .brand-dot { fill: var(--brand-green); }
</style>
</head>
<body>
  <svg class="banner" viewBox="0 0 1200 450" xmlns="http://www.w3.org/2000/svg">
    <title>60th Anniversary – Meridian Inks</title>
    <rect class="band band--top" x="0" y="0" width="1200" height="30"/>

    <text class="headline headline__number" x="182" y="282"
          textLength="150" lengthAdjust="spacingAndGlyphs">60</text>
    <text class="headline headline__ordinal" x="338" y="196"
          textLength="72" lengthAdjust="spacingAndGlyphs">th</text>
    <text class="headline headline__word" x="458" y="282"
          textLength="652" lengthAdjust="spacingAndGlyphs">Anniversary</text>

    <g class="brand">
      <circle class="brand-dot" cx="774" cy="336" r="13"/>
      <text class="brand-name" x="800" y="324"
            textLength="200" lengthAdjust="spacingAndGlyphs">Meridian</text>
      <text class="brand-name" x="1000" y="362" text-anchor="end"
            textLength="76" lengthAdjust="spacingAndGlyphs">Inks</text>
    </g>

    <rect class="band band--bottom" x="0" y="420" width="1200" height="30"/>
  </svg>
</body>
</html>
```